Real Estate Listing Landing Page

I am looking for a landing page for my Flat Fee MLS Listing website... The name of my website is "Brightkey Home Sales".

I am a big fan of this landing page setup and would like something similar.
https://quaylinehomes.com/

I am a fan of the design style on https://quaylinehomes.com/ and also this design style as well... https://2817.velmontedge.com/

Use your creativity and incorporate your own twists that you would feel lift up this landing pages' appeal. I'd love some red color incorporated within the design.

Target Market(s)

Real Estate Home Sellers

Industry/Entity Type

Real Estate

Coding

Coded - Design and coding required

Font styles to use
Sans Serif

Colors
0054AA
0677BA
7BADD7
CADEEF
E8F1F8
0094D4
00A9DD
6FCCEA
C7EBF8
E9F6FB
EB3D1F
EC4F4E
F09395
F8D3D4
FCEDEE

```html
<!DOCTYPE html>
<html lang="en">
<head>
<meta charset="utf-8">
<title>Brightkey Home Sales – Flat Fee MLS Florida</title>
<link href="https://fonts.googleapis.com/css2?family=Poppins:wght@400;500;600;700&family=Montserrat:wght@400;500&display=swap" rel="stylesheet">
<style>
  :root{
    --red:#e0262b;
    --red-soft:#eb3d1f;
    --ink:#1e1e1e;
    --text:#2c2c2c;
    --muted:#555;
    --line:#c9c9c9;
    --panel:#f4f4f4;
    --pill:#2e2e2e;
    --faint:#ececec;
  }
  *{box-sizing:border-box;margin:0;padding:0}
  html,body{width:829px;height:1200px;overflow:hidden;background:#fff}
  body{position:relative;font-family:"Poppins",sans-serif;color:var(--text)}
  .abs{position:absolute}

  /* top bar */
  .topbar{left:0;top:0;width:829px;height:21px;border-bottom:1px solid #8a8a8a}
  .topbar .contacts{position:absolute;right:88px;top:6px;display:flex;align-items:center;gap:14px}
  .topbar .contact{font-size:6.4px;display:flex;align-items:center;gap:4px;color:var(--ink);white-space:nowrap;line-height:1}
  .topbar svg{width:8px;height:8px;flex:none}

  /* header */
  .brand{left:8px;top:30px;display:flex;align-items:center;gap:4px}
  .brand .mark{width:9px;height:9px;background:var(--red)}
  .brand .name{font-size:11.5px;font-weight:600;letter-spacing:1px;color:var(--ink)}
  .nav{top:41px;left:255px;display:flex;align-items:center;font-size:7px;font-weight:500;color:var(--ink)}
  .nav a{color:inherit;text-decoration:none;margin-right:15.5px;white-space:nowrap}
  .nav a.active{background:var(--red);color:#fff;padding:4px 11px 4px 10px;clip-path:polygon(0 0,100% 0,100% 100%,8% 100%);margin-right:5px}
  .account{top:31px;left:686px;font-size:6px;font-weight:500;color:var(--ink)}
  .cta-list{left:649px;top:48px;width:92px;height:19px;border-radius:10px;background:var(--red);color:#fff;font-size:6.6px;font-weight:600;display:flex;align-items:center;justify-content:center;gap:5px}
  .cta-list svg{width:11px;height:11px}

  /* hero */
  .hero{left:0;top:76px;width:829px;height:272px;background:linear-gradient(180deg,#9fb4c4 0%,#d8dcdc 45%,#8a9a6a 80%,#5e7a3c 100%)}

  /* intro */
  .intro{left:0;top:348px;width:829px;height:351px;background:var(--panel)}
  .intro h1{position:absolute;left:87px;top:68px;font-size:31px;line-height:36.5px;font-weight:700;color:var(--ink);letter-spacing:-.2px}
  .intro p{position:absolute;left:88px;top:186px;width:318px;font-family:"Montserrat",sans-serif;font-size:8.25px;line-height:14.8px;color:#333}
  .sketch{left:444px;top:415px;width:305px;height:203px;background:linear-gradient(135deg,#efefef,#e6e6e6);opacity:.8}

  /* steps */
  .steps-title{left:0;top:728px;width:829px;text-align:center;font-size:23px;font-weight:700;color:var(--ink)}
  .steps-sub{left:0;top:763px;width:829px;text-align:center;font-size:9px;line-height:11.5px;color:var(--ink)}
  .card{border:1.5px solid var(--line);border-radius:3px;background:#fff}
  .card .num{position:absolute;left:8px;top:4px;font-size:56px;font-weight:700;color:var(--faint);line-height:1}
  .card h3{position:absolute;left:50px;top:9px;font-size:13.5px;font-weight:500;color:var(--ink);white-space:nowrap}
  .card ul{position:absolute;left:50px;top:34px;right:20px;list-style:none;font-size:6.9px;line-height:11px;color:var(--muted)}
  .card li{position:relative;padding-left:12px;margin-bottom:4px}
  .card li svg{position:absolute;left:0;top:2px;width:8px;height:8px}
  .card li.strong{font-weight:600;color:var(--ink)}

  /* buttons */
  .pill{top:1070px;height:33px;border-radius:17px;background:var(--pill);color:#fff;font-size:11.5px;display:flex;align-items:center;justify-content:center;gap:8px;box-shadow:0 3px 5px rgba(0,0,0,.25);text-decoration:none}
  .pill svg{width:14px;height:14px}

  /* valuation band */
  .band{left:0;top:1142px;width:829px;height:58px;background:var(--red);overflow:hidden}
  .band .stripe{position:absolute;left:-30px;top:0;width:140px;height:58px;background:linear-gradient(160deg,rgba(255,255,255,.55),rgba(255,255,255,0) 60%);clip-path:polygon(0 0,25% 0,100% 100%,60% 100%)}
  .band h2{position:absolute;left:373px;top:43px;font-size:23px;font-weight:700;color:#fff;letter-spacing:.5px;white-space:nowrap}
</style>
</head>
<body>

<header>
  <div class="abs topbar">
    <div class="contacts">
      <div class="contact">
        <svg viewBox="0 0 16 12"><rect x="0.5" y="0.5" width="15" height="11" rx="1" fill="#222"/><path d="M1 1l7 6 7-6" stroke="#fff" stroke-width="1.4" fill="none"/></svg>
        info@brightkeyhomesales.com
      </div>
      <div class="contact">
        <svg viewBox="0 0 24 24"><path fill="#222" d="M6.6 10.8a15.1 15.1 0 0 0 6.6 6.6l2.2-2.2c.3-.3.7-.4 1-.2 1.1.4 2.3.6 3.6.6.6 0 1 .4 1 1V20c0 .6-.4 1-1 1A17 17 0 0 1 3 4c0-.6.4-1 1-1h3.5c.6 0 1 .4 1 1 0 1.3.2 2.5.6 3.6.1.3 0 .7-.2 1z"/></svg>
        555-214-0386
      </div>
    </div>
  </div>

  <div class="abs brand"><span class="mark"></span><span class="name">HARBORLINE</span></div>

  <nav class="abs nav">
    <a class="active" href="#">HOME</a>
    <a href="#">HOW IT WORKS</a>
    <a href="#">PRICING</a>
    <a href="#">WHY WE'RE BETTER</a>
    <a href="#">FAQ</a>
    <a href="#">CONTACT US</a>
  </nav>

  <div class="abs account">LOGIN &nbsp;/&nbsp; SIGN UP</div>
  <div class="abs cta-list">
    <svg viewBox="0 0 24 24" fill="none" stroke="#fff" stroke-width="1.6"><path d="M3 11l9-7 9 7"/><path d="M6 10v10h12V10"/><rect x="10" y="14" width="4" height="6"/></svg>
    LIST YOUR HOME!
  </div>
</header>

<div class="abs hero" role="img" aria-label="Photo of white apartment buildings with gardens and a sold sign in front"></div>

<section class="abs intro">
  <h1>FLAT FEE MLS<br>MULTIPLE LISTING<br>SERVICE FLORIDA</h1>
  <p>Brightkey Home Sales is here to provide you with Flat Fee MLS Listings for as low as $79! We are powered by real estate brokerage company, Harborline Realty, and we pride in our superior service when it comes to helping clients save thousands of dollars throughout their real estate transactions. We are a dedicated team that services Palm Beach County, Broward County, St Lucie County and all of the Miami-Dade County and areas. We have vast knowledge in these areas and can provide you, as a client, a comforting and smooth real estate transaction.</p>
</section>
<div class="abs sketch" role="img" aria-label="Faint line sketch of a modern house"></div>

<section>
  <h2 class="abs steps-title">SELLING STEPS YOUR FLORIDA HOME EASY.</h2>
  <p class="abs steps-sub">From the time you submit your listing inquiry to finalizing the<br>sale of your home, our team of experts will assist you throughout the entire home selling process.</p>

  <div class="abs card" style="left:88px;top:819px;width:316px;height:95px">
    <span class="num">1</span>
    <h3>Sell Your Home Fast for Top Dollar!</h3>
    <ul>
      <li><svg viewBox="0 0 16 16" fill="none" stroke="#444"><circle cx="8" cy="8" r="7"/><path d="M7 5l3 3-3 3"/></svg>For as low as $79, we provide you with every tool you need to list and sell your home on the MLS quickly and for top dollar.</li>
      <li><svg viewBox="0 0 16 16" fill="none" stroke="#444"><circle cx="8" cy="8" r="7"/><path d="M7 5l3 3-3 3"/></svg>Unlimited photos! Add as many as the MLS will allow.</li>
    </ul>
  </div>

  <div class="abs card" style="left:425px;top:819px;width:316px;height:95px">
    <span class="num">2</span>
    <h3>Licensed Brokerage Company</h3>
    <ul>
      <li><svg viewBox="0 0 16 16" fill="none" stroke="#444"><circle cx="8" cy="8" r="7"/><path d="M7 5l3 3-3 3"/></svg>Brightkey Home Sales is powered by Harborline Realty, a licensed Florida real estate brokerage company.</li>
      <li><svg viewBox="0 0 16 16" fill="none" stroke="#444"><circle cx="8" cy="8" r="7"/><path d="M7 5l3 3-3 3"/></svg>Access to a licensed broker if you need help!</li>
    </ul>
  </div>

  <div class="abs card" style="left:88px;top:936px;width:316px;height:104px">
    <span class="num">3</span>
    <h3>No Hidden Fees, Serious Savings</h3>
    <ul>
      <li><svg viewBox="0 0 16 16" fill="none" stroke="#444"><circle cx="8" cy="8" r="7"/><path d="M7 5l3 3-3 3"/></svg>There are no hidden fees or surprises. You pay one low fee, and let us handle the rest.</li>
      <li><svg viewBox="0 0 16 16" fill="none" stroke="#444"><circle cx="8" cy="8" r="7"/><path d="M7 5l3 3-3 3"/></svg>Cancel anytime – no cancellation fees!</li>
    </ul>
  </div>

  <div class="abs card" style="left:425px;top:936px;width:316px;height:104px">
    <span class="num">4</span>
    <h3>We're Here For You</h3>
    <ul>
      <li><svg viewBox="0 0 16 16" fill="none" stroke="#444"><circle cx="8" cy="8" r="7"/><path d="M7 5l3 3-3 3"/></svg>With support by phone or email, our dedicated staff is always available and happy to help.</li>
      <li><svg viewBox="0 0 16 16" fill="none" stroke="#444"><circle cx="8" cy="8" r="7"/><path d="M7 5l3 3-3 3"/></svg>Unlimited changes to your listing!</li>
      <li class="strong"><svg viewBox="0 0 16 16" fill="none" stroke="#444"><circle cx="8" cy="8" r="7"/><path d="M7 5l3 3-3 3"/></svg>You get 1% cash back when you buy your next home.</li>
    </ul>
  </div>

  <a class="abs pill" href="#" style="left:275px;width:147px">LIST YOUR PROPERTY</a>
  <a class="abs pill" href="#" style="left:437px;width:126px">
    <svg viewBox="0 0 24 24"><path fill="#fff" d="M6.6 10.8a15.1 15.1 0 0 0 6.6 6.6l2.2-2.2c.3-.3.7-.4 1-.2 1.1.4 2.3.6 3.6.6.6 0 1 .4 1 1V20c0 .6-.4 1-1 1A17 17 0 0 1 3 4c0-.6.4-1 1-1h3.5c.6 0 1 .4 1 1 0 1.3.2 2.5.6 3.6.1.3 0 .7-.2 1z"/></svg>
    555-214-0386
  </a>
</section>

<section class="abs band">
  <span class="stripe"></span>
  <h2>WHAT'S MY HOME WORTH?</h2>
</section>

</body>
</html>
```